Business card for Eyelash extension salon in Marlow Hills,California USA

We need new business card for our salon in Marlow Hills. The salon name is 'Lumarra' . We would like to have...Business name: Lumarra Name of person: will provide later Address 6128 N.Corbel Ridge Blvd Marlow Hills , CA 90299 Phone: will provide later (Text only) Web: www.lumarrastudio-example.com Pictogrid icon, Friendvale icon follow us for seasonal campaign and news @lumarrastudioexample Design should look elegant, high-end, clean, simple, cohesive with my brand. Please refer my brand board. Business name color will be metallic bronzy color. Im thinking grey background or white background. Thanks

Target Market(s)

25-35. Gender neutral. People who are in Entertainment business industry.
This is High-end Eyelash extension salon in Marlow Hills

Industry/Entity Type

Beauty Salon

Contact Information for Business Card

Business name: Lumarra
Name of person: will provide later
Address 6128 N.Corbel Ridge Blvd Marlow Hills , CA 90299
Phone: will provide later (Text only)
Web: www.lumarrastudio-example.com
Pictogrid icon, Friendvale icon
follow us for seasonal campaign and news @lumarrastudioexample

Requirements
Must have
• Beautiful, elegant, clean and simple look but very attractive and modern
Should not have
• We don't like too clutter, too busy designs.

```html
<!DOCTYPE html>
<html lang="en">
<head>
<meta charset="utf-8">
<title>Lumarra Marlow Hills – Business Card</title>
<link rel="stylesheet" href="https://fonts.googleapis.com/css2?family=Bodoni+Moda:wght@400;600;900&family=Josefin+Sans:wght@400&display=swap">
<style>
  :root {
    --page: #ffffff;
    --sand: #c9ac91;
    --cocoa: #8a6650;
    --bronze: #8d6a52;
    --gold-strip: #b99066;
    --ink: #111111;
    --paper: #ffffff;
    --shadow: rgba(0, 0, 0, 0.55);
  }
  * { margin: 0; padding: 0; box-sizing: border-box; }
  html, body { width: 1200px; height: 900px; overflow: hidden; background: var(--page); }
  .canvas { position: relative; width: 1200px; height: 900px; }

  .card {
    position: absolute;
    width: 613px;
    height: 340px;
    overflow: hidden;
    box-shadow: 9px 9px 9px var(--shadow);
  }

  /* Front */
  .card--front { left: 89px; top: 80px; background: var(--sand); }
  .front__bar { position: absolute; width: 21px; background: var(--cocoa); }
  .front__bar--left { left: 0; top: 20px; bottom: 0; }
  .front__bar--right { right: 0; top: 20px; height: 298px; }

  .wordmark {
    position: absolute;
    font-family: "Bodoni Moda", serif;
    font-weight: 400;
    color: var(--bronze);
    line-height: 1;
    white-space: nowrap;
  }
  .tagline {
    position: absolute;
    font-family: "Josefin Sans", sans-serif;
    color: var(--bronze);
    letter-spacing: 0.16em;
    white-space: nowrap;
  }
  .card--front .wordmark { left: 0; right: 0; top: 132px; text-align: center; font-size: 100px; }
  .card--front .tagline { left: 301px; top: 258px; font-size: 15px; }

  /* Back */
  .card--back { left: 392px; top: 487px; background: var(--paper); }
  .back__bar { position: absolute; left: 0; top: 21px; width: 21px; height: 298px; background: var(--sand); }
  .back__panel { position: absolute; left: 306px; top: 0; right: 0; bottom: 0; background: var(--sand); }
  .card--back .wordmark { left: 30px; width: 260px; top: 128px; text-align: center; font-size: 56px; }
  .card--back .tagline { left: 151px; top: 224px; font-size: 10px; }

  .holder-name {
    position: absolute;
    left: 327px;
    top: 18px;
    font-family: "Bodoni Moda", serif;
    font-weight: 900;
    font-size: 30px;
    letter-spacing: 0.19em;
    white-space: nowrap;
    color: var(--ink);
  }

  .icon-strip {
    position: absolute;
    left: 289px;
    top: 95px;
    width: 35px;
    height: 149px;
    background: var(--gold-strip);
  }
  .icon-strip svg { position: absolute; left: 7px; width: 21px; height: 21px; }

  .contact {
    position: absolute;
    left: 328px;
    font-family: "Bodoni Moda", serif;
    font-weight: 600;
    font-size: 13px;
    line-height: 1.25;
    white-space: nowrap;
    color: var(--ink);
  }
  .contact--phone { top: 100px; }
  .contact--web { top: 141px; }
  .contact--address { top: 179px; }
  .contact--social { top: 227px; }
</style>
</head>
<body>
<main class="canvas">

  <section class="card card--front" aria-label="Business card front">
    <div class="front__bar front__bar--left"></div>
    <div class="front__bar front__bar--right"></div>
    <div class="wordmark">Lumarra</div>
    <div class="tagline">MARLOW HILLS</div>
  </section>

  <section class="card card--back" aria-label="Business card back">
    <div class="back__bar"></div>
    <div class="wordmark">Lumarra</div>
    <div class="tagline">MARLOW HILLS</div>

    <div class="back__panel"></div>
    <h1 class="holder-name">YOUR NAME</h1>

    <div class="icon-strip">
      <svg style="top:5px" viewBox="0 0 24 24" aria-label="Phone">
        <path fill="#fff" d="M3 9c0-3 4-5 9-5s9 2 9 5v1.5h-4V8.5c-1.5-.6-3-.8-5-.8s-3.5.2-5 .8v2H3z"/>
        <rect x="5" y="11" width="14" height="9" rx="1.5" fill="#fff"/>
        <circle cx="12" cy="15.5" r="2.2" fill="var(--gold-strip)"/>
      </svg>
      <svg style="top:45px" viewBox="0 0 24 24" aria-label="Website">
        <g fill="none" stroke="#fff" stroke-width="1.6">
          <circle cx="12" cy="12" r="9"/>
          <ellipse cx="12" cy="12" rx="4" ry="9"/>
          <path d="M3 12h18M4.5 7.5h15M4.5 16.5h15"/>
        </g>
      </svg>
      <svg style="top:90px" viewBox="0 0 24 24" aria-label="Address">
        <path fill="#fff" d="M12 2a7 7 0 0 0-7 7c0 5.2 7 13 7 13s7-7.8 7-13a7 7 0 0 0-7-7z"/>
        <circle cx="12" cy="9" r="2.6" fill="var(--gold-strip)"/>
      </svg>
      <svg style="top:130px" viewBox="0 0 24 24" aria-label="Friendvale and Pictogrid">
        <rect x="2" y="8" width="8" height="8" fill="#fff"/>
        <circle cx="18" cy="12" r="4" fill="none" stroke="#fff" stroke-width="1.5"/>
      </svg>
    </div>

    <p class="contact contact--phone">123 456 789</p>
    <p class="contact contact--web">www.lumarrastudio-example.com</p>
    <p class="contact contact--address">6128 N.Corbel Ridge Blvd Marlow Hills,<br>CA 90299</p>
    <p class="contact contact--social">@lumarrastudioexample</p>
  </section>

</main>
</body>
</html>
```